Valentine's Day menu

Our establishment on 57, (bar - brasserie - wine bar); Offers a menu for Valentine's Day, one that will be on site and another in delivery.

Menu on site:

Starter: Oysters, warm champagne flambé

Dish: Grilled tournedos, braised endives and Jerusalem artichokes
Ranger Sauce
Sole meunière, lemon sauce, steamed potatoes, rice

Dessert: Tiramisu with red fruits - Flambéed Crêpe Suzette

Menu at 29.90€

Delivery menu: Raclette platter with Savoy cheeses - Pierrade platter and fresh vegetables.
Half-bottle of VALDORIEUX BLANCS DE BLANS.

Please use the Valentine's Day theme, use our logo and colors (attached). The goal is to get as many reservations as possible.

Reservation required at: 06 38 72 15 09
57
18 rue Fernand Gaudry 71840 BRÉVANNE

I remain at your disposal.

- Rate ; 45€ / Person

```html
<!DOCTYPE html>
<html lang="en">
<head>
<meta charset="utf-8">
<title>Maison Cerise – Valentine's Day Menus</title>
<link href="https://fonts.googleapis.com/css2?family=Great+Vibes&family=Playfair+Display:wght@700;900&family=Montserrat:wght@400;500;600&display=swap" rel="stylesheet">
<style>
  :root {
    --page: #f1efec;
    --wine-deep: #3a040a;
    --wine: #6a0914;
    --wine-bright: #8e111f;
    --gold: #e3b64a;
    --gold-light: #f6dc86;
    --gold-dark: #a9781e;
    --cream: #fff7ea;
    --ink-dark: #4a2a08;
  }
  * { box-sizing: border-box; margin: 0; padding: 0; }
  html, body { width: 693px; height: 1200px; overflow: hidden; }
  body {
    background: var(--page);
    font-family: "Montserrat", sans-serif;
    color: var(--cream);
    position: relative;
  }

  .flyer {
    position: absolute;
    left: 121px;
    width: 451px;
    height: 578px;
    background:
      repeating-linear-gradient(90deg, rgba(0,0,0,0.10) 0 18px, rgba(255,255,255,0.02) 18px 36px),
      radial-gradient(ellipse at 50% 45%, var(--wine-bright) 0%, var(--wine) 45%, var(--wine-deep) 100%);
    box-shadow: -4px 4px 0 #3b3b3b;
    overflow: hidden;
  }
  .flyer--site { top: 12px; }
  .flyer--delivery { top: 610px; }

  .flyer__frame {
    position: absolute;
    inset: 18px 20px;
    border: 1.5px solid var(--gold);
    pointer-events: none;
  }
  .corner-dot {
    position: absolute;
    width: 9px; height: 9px;
    border-radius: 50%;
    background: var(--gold);
  }
  .corner-dot--tl { top: 12px; left: 14px; }
  .corner-dot--tr { top: 12px; right: 14px; }
  .corner-dot--bl { bottom: 12px; left: 14px; }
  .corner-dot--br { bottom: 12px; right: 14px; }

  .heart-cluster {
    position: absolute;
    border-radius: 50%;
    background: radial-gradient(circle, rgba(181,20,42,0.75) 0%, rgba(181,20,42,0.35) 45%, rgba(181,20,42,0) 72%);
  }

  .flyer__content {
    position: absolute;
    inset: 26px 40px 24px;
    display: flex;
    flex-direction: column;
    align-items: center;
    text-align: center;
  }

  .brand {
    margin-top: 22px;
    font-family: "Montserrat", sans-serif;
    font-weight: 500;
    font-size: 15px;
    letter-spacing: 1.5px;
    color: var(--gold);
    white-space: nowrap;
    line-height: 1.2;
  }

  .title {
    font-family: "Great Vibes", cursive;
    font-weight: 400;
    font-size: 38px;
    color: #ffffff;
    line-height: 1;
    margin-top: 14px;
  }
  .flyer--delivery .title { font-size: 46px; margin-top: 26px; }

  .menu-tag {
    margin-top: 10px;
    padding: 3px 16px 2px;
    border: 1.5px solid var(--gold);
    outline: 1px solid var(--gold-dark);
    outline-offset: 2px;
    font-family: "Playfair Display", serif;
    font-weight: 900;
    font-size: 18px;
    color: var(--gold-light);
    letter-spacing: 0.5px;
  }
  .flyer--delivery .menu-tag { font-size: 24px; padding: 3px 16px; margin-top: 20px; }

  .course { margin-top: 16px; }
  .course__label {
    display: inline-block;
    min-width: 130px;
    padding: 2px 0;
    border-top: 1px solid var(--gold);
    border-bottom: 1px solid var(--gold);
    font-size: 10px;
    font-weight: 500;
    letter-spacing: 2.5px;
    color: #ffffff;
  }
  .course__items {
    margin-top: 6px;
    font-size: 8.4px;
    line-height: 1.5;
    color: #f3e6df;
  }

  .delivery-list { list-style: none; margin-top: 24px; width: 220px; }
  .delivery-list li {
    font-size: 9px;
    color: #ffffff;
    padding: 10px 0;
    border-bottom: 1.5px dotted var(--gold);
  }
  .delivery-list li:last-child { border-bottom: none; }

  .price-wrap { margin-top: 14px; }
  .price {
    position: relative;
    margin: 4px auto;
    width: 186px;
    height: 30px;
    display: flex; align-items: center; justify-content: center;
  }
  .flyer--delivery .price { width: 270px; height: 36px; }
  .price svg { position: absolute; inset: 0; width: 100%; height: 100%; }
  .price__text {
    position: relative;
    font-family: "Playfair Display", serif;
    font-weight: 700;
    font-size: 12px;
    color: var(--ink-dark);
    letter-spacing: 0.5px;
  }
  .price__text--rate {
    font-family: "Montserrat", sans-serif;
    font-weight: 600;
    font-size: 11px;
  }
  .price__amount { font-size: 22px; font-weight: 700; margin: 0 3px; }
  .price__rule { width: 180px; height: 1px; background: var(--gold); margin: 0 auto; }

  .contact {
    margin-top: auto;
    margin-bottom: 24px;
    display: flex;
    align-items: flex-start;
    gap: 6px;
    font-size: 8.6px;
    font-weight: 600;
    color: #ffffff;
    text-align: left;
    line-height: 1.3;
  }
  .contact__item { display: flex; gap: 4px; align-items: flex-start; }
  .contact__item svg { width: 9px; height: 10px; margin-top: 1px; flex: none; }
  .contact__divider { width: 1px; height: 22px; background: var(--gold); }
</style>
</head>
<body>

<section class="flyer flyer--site">
  <div class="heart-cluster" style="left:18px;top:20px;width:120px;height:130px" role="img" aria-label="Red balloon hearts with gold heart outlines"></div>
  <div class="heart-cluster" style="right:18px;top:20px;width:120px;height:120px" role="img" aria-label="Red balloon hearts with gold heart outlines"></div>
  <div class="heart-cluster" style="left:10px;top:250px;width:90px;height:120px" role="img" aria-label="Red balloon hearts with gold heart outline"></div>
  <div class="heart-cluster" style="right:12px;top:210px;width:100px;height:110px" role="img" aria-label="Red balloon hearts with gold heart outline"></div>
  <div class="flyer__frame"></div>
  <span class="corner-dot corner-dot--tl"></span><span class="corner-dot corner-dot--tr"></span>
  <span class="corner-dot corner-dot--bl"></span><span class="corner-dot corner-dot--br"></span>

  <div class="flyer__content">
    <div class="brand">MAISON CERISE</div>
    <h1 class="title">Valentine's Day</h1>
    <div class="menu-tag">SITE MENU:</div>

    <div class="course">
      <div class="course__label">STARTER</div>
      <p class="course__items">Oysters, warm champagne flambé</p>
    </div>
    <div class="course">
      <div class="course__label">DISH</div>
      <p class="course__items">Grilled tournedos, braised endives and Jerusalem artichokes<br>Ranger Sauce Sole meunière, lemon sauce, steamed potatoes, rice</p>
    </div>
    <div class="course">
      <div class="course__label">DESSERT</div>
      <p class="course__items">Tiramisu with red fruits - Flambéed Crêpe Suzette</p>
    </div>

    <div class="price-wrap">
      <div class="price__rule"></div>
      <div class="price">
        <svg viewBox="0 0 186 30" preserveAspectRatio="none" aria-hidden="true">
          <defs><linearGradient id="goldA" x1="0" x2="1"><stop offset="0" stop-color="#b8862a"/><stop offset="0.5" stop-color="#f7dc8a"/><stop offset="1" stop-color="#b8862a"/></linearGradient></defs>
          <polygon points="0,0 186,0 176,15 186,30 0,30 10,15" fill="url(#goldA)"/>
        </svg>
        <span class="price__text">MENU AT 29.90€</span>
      </div>
      <div class="price__rule"></div>
    </div>

    <div class="contact">
      <div class="contact__item">
        <svg viewBox="0 0 10 10" aria-hidden="true"><path d="M2 1l2 2-1 1.2c.6 1.2 1.5 2.1 2.7 2.7L7 6l2 2-1.4 1.4C4.6 9.4.6 5.4.6 2.4z" fill="none" stroke="#fff" stroke-width="0.9"/></svg>
        <span>Reservation required at:<br>06 38 72 15 09</span>
      </div>
      <span class="contact__divider"></span>
      <div class="contact__item">
        <svg viewBox="0 0 10 12" aria-hidden="true"><path d="M5 11S1.5 7 1.5 4.5a3.5 3.5 0 0 1 7 0C8.5 7 5 11 5 11z" fill="none" stroke="#fff" stroke-width="0.9"/><circle cx="5" cy="4.5" r="1.2" fill="#fff"/></svg>
        <span>18 rue Fernand Gaudry<br>71840 BRÉVANNE</span>
      </div>
    </div>
  </div>
</section>

<section class="flyer flyer--delivery">
  <div class="heart-cluster" style="left:18px;top:20px;width:120px;height:130px" role="img" aria-label="Red balloon hearts with gold heart outlines"></div>
  <div class="heart-cluster" style="right:16px;top:20px;width:150px;height:140px" role="img" aria-label="Red balloon hearts with gold heart outlines"></div>
  <div class="heart-cluster" style="left:0;bottom:40px;width:100px;height:150px" role="img" aria-label="Red balloon hearts with gold heart outline"></div>
  <div class="heart-cluster" style="right:0;bottom:30px;width:130px;height:140px" role="img" aria-label="Red balloon hearts with gold heart outline"></div>
  <div class="flyer__frame"></div>
  <span class="corner-dot corner-dot--tl"></span><span class="corner-dot corner-dot--tr"></span>
  <span class="corner-dot corner-dot--bl"></span><span class="corner-dot corner-dot--br"></span>

  <div class="flyer__content">
    <div class="brand">MAISON CERISE</div>
    <h1 class="title">Valentine's Day</h1>
    <div class="menu-tag">DELIVERY MENU:</div>

    <ul class="delivery-list">
      <li>Raclette platter with Savoy cheeses</li>
      <li>Pierrade platter and fresh vegetables.</li>
      <li>Half-bottle of VALDORIEUX BLANCS DE BLANS.</li>
    </ul>

    <div class="price-wrap">
      <div class="price__rule"></div>
      <div class="price">
        <svg viewBox="0 0 270 36" preserveAspectRatio="none" aria-hidden="true">
          <defs><linearGradient id="goldB" x1="0" x2="1"><stop offset="0" stop-color="#b8862a"/><stop offset="0.5" stop-color="#f7dc8a"/><stop offset="1" stop-color="#b8862a"/></linearGradient></defs>
          <polygon points="0,0 270,0 256,18 270,36 0,36 14,18" fill="url(#goldB)"/>
        </svg>
        <span class="price__text price__text--rate">RATE :<span class="price__amount">45€</span>/ PERSON</span>
      </div>
      <div class="price__rule"></div>
    </div>

    <div class="contact">
      <div class="contact__item">
        <svg viewBox="0 0 10 10" aria-hidden="true"><path d="M2 1l2 2-1 1.2c.6 1.2 1.5 2.1 2.7 2.7L7 6l2 2-1.4 1.4C4.6 9.4.6 5.4.6 2.4z" fill="none" stroke="#fff" stroke-width="0.9"/></svg>
        <span>Reservation required at:<br>06 38 72 15 09</span>
      </div>
      <span class="contact__divider"></span>
      <div class="contact__item">
        <svg viewBox="0 0 10 12" aria-hidden="true"><path d="M5 11S1.5 7 1.5 4.5a3.5 3.5 0 0 1 7 0C8.5 7 5 11 5 11z" fill="none" stroke="#fff" stroke-width="0.9"/><circle cx="5" cy="4.5" r="1.2" fill="#fff"/></svg>
        <span>18 rue Fernand Gaudry<br>71840 BRÉVANNE</span>
      </div>
    </div>
  </div>
</section>

</body>
</html>
```